Wordpress Design - Accounting Practice Startup

We are a relatively new Accounting Firm in Sydney with a primary focus on the Not-For-Profit sector. We need a complete re-design of our wordpress based website: www.tallowmereledger.com.au
We already have a logo design which we would like to keep using. See uploaded files.
We have a simple menu stucture:
- Home
- About Us
- Our Services
- Contact Us
(Suggestions welcome!)
Happy for it to be a single page scrolling website linked via the menu. We would like the "Our Services" page/section to have icons for the following:
- Bookkeeping
- Payroll
- Accounting
- Training
- Consulting
- Projects
We'd like a banner at the top of the page below the menu, and a place for testimonials, possibly integrated into the body or to the side. Images and icons to be included would be great.
Our main aim is to have an elegant and modern website that works well on all devices.
Updates
Industry/Entity Type
Accounting
Colors
Designer to choose colors to be used in the design.
Look and feel
Each slider illustrates characteristics of the customer's brand and the style your logo design should communicate.

```html
<!DOCTYPE html>
<html lang="en">
<head>
<meta charset="utf-8">
<title>Tallowmere Ledger</title>
<link href="https://fonts.googleapis.com/css2?family=Poppins:wght@400;500;600&family=Open+Sans:wght@400;600&family=Oswald:wght@500&display=swap" rel="stylesheet">
<style>
:root{
  --green:#3b9e3b;
  --green-dark:#2f8a31;
  --ink:#2a2d31;
  --slate:#4f555d;
  --text:#6d7077;
  --muted:#9a9da3;
  --paper:#ffffff;
  --mist:#eeeff1;
  --footer:#2b2e33;
}
*{margin:0;padding:0;box-sizing:border-box}
html,body{width:1200px;height:2711px;overflow:hidden}
body{position:relative;background:var(--mist);font-family:"Open Sans",Arial,sans-serif;color:var(--text)}
.abs{position:absolute}
.hero-photo{left:0;top:0;width:1200px;height:570px;background:linear-gradient(135deg,#2f3236 0%,#55595f 45%,#7a7e84 70%,#45484d 100%)}
.cloud-photo{left:0;top:2250px;width:1200px;height:230px;background:linear-gradient(180deg,var(--mist) 0%,#e4e8ed 40%,#c3ccd6 75%,#9aa6b3 100%)}
.shapes{left:0;top:0;z-index:1}
.layer{z-index:2}
.h{font-family:"Poppins",Arial,sans-serif}

/* header */
.brand{left:155px;top:28px;display:flex;align-items:center;gap:10px;color:#fff;font-family:"Poppins",sans-serif;font-weight:600;font-size:20px;line-height:1}
.brand-mark{width:22px;height:22px;background:var(--green)}
.main-nav{left:388px;top:40px;display:flex;gap:30px;font-family:"Poppins",sans-serif;font-size:11px;letter-spacing:.5px;color:#fff}
.main-nav .active::before{content:"-- "}
.main-nav .active::after{content:" -"}
.phone{left:790px;top:34px;font-family:"Oswald",sans-serif;font-weight:500;font-size:17px;color:#fff}
.login{left:949px;top:31px;width:94px;height:33px;background:var(--green);color:#fff;font-family:"Poppins",sans-serif;font-size:11px;font-weight:600;display:flex;align-items:center;justify-content:center;gap:6px}
.login i{width:10px;height:10px;border-radius:50%;background:#fff;display:block}

/* hero */
.hero-title{left:155px;top:197px;color:#fff;font-family:"Poppins",sans-serif;font-weight:500;font-size:25px;line-height:31px}
.hero-copy{left:155px;top:274px;width:440px;color:#fff;font-size:15px;line-height:21px}
.btn-light{left:155px;top:346px;width:129px;height:34px;background:#fff;color:var(--ink);font-family:"Poppins",sans-serif;font-size:10px;letter-spacing:1px;display:flex;align-items:center;justify-content:center}
.slide-dots{left:1010px;top:208px;display:flex;flex-direction:column;gap:10px}
.slide-dots span{width:14px;height:14px;border-radius:50%;border:2px solid #fff;display:block}
.slide-dots .on{background:var(--green);border-color:#fff}

/* testimonial */
.quote-mark{left:0;width:1200px;top:568px;text-align:center;color:var(--green);font-family:"Poppins",sans-serif;font-weight:600;font-size:56px;line-height:1}
.quote-text{left:310px;width:580px;top:630px;text-align:center;font-size:16px;line-height:24px;color:#6b6e74}
.quote-author{left:500px;width:200px;top:730px;text-align:center}
.quote-author b{display:block;color:var(--green);font-family:"Poppins",sans-serif;font-size:13px;font-weight:600}
.quote-author span{font-size:11px;letter-spacing:1px;color:#777}

/* section heads */
.kicker{left:0;width:1200px;text-align:center;font-family:"Poppins",sans-serif;font-size:9px;letter-spacing:1.5px;color:#555}
.title{left:0;width:1200px;text-align:center;font-family:"Poppins",sans-serif;font-size:19px;font-weight:600;color:var(--ink);text-transform:uppercase}
.title em{font-style:normal;color:var(--green)}
.dash{left:585px;width:30px;border-top:1px dashed var(--muted)}

.about-copy{left:265px;width:670px;top:997px;text-align:center;font-size:12.5px;line-height:19.5px;color:#777}
.btn-outline{left:535px;top:1110px;width:128px;height:34px;border:1px solid var(--green);background:#fff;color:var(--ink);font-family:"Poppins",sans-serif;font-size:10px;letter-spacing:1px;display:flex;align-items:center;justify-content:center}

/* services */
.card{width:280px;height:264px;background:var(--paper);border-bottom:4px solid var(--slate);box-shadow:0 2px 8px rgba(0,0,0,.06);text-align:center}
.card.featured{border-bottom-color:var(--green)}
.card h3{position:absolute;left:0;width:100%;top:102px;font-family:"Poppins",sans-serif;font-size:15px;font-weight:600;color:var(--ink)}
.card.featured h3{color:var(--green)}
.card p{position:absolute;left:22px;right:22px;top:135px;font-size:12.5px;line-height:18px;color:#777}
.card a{position:absolute;left:0;width:100%;top:215px;font-family:"Poppins",sans-serif;font-size:9.5px;letter-spacing:1px;color:var(--ink);text-decoration:none}
.card a span{border-bottom:1px dashed #777;padding-bottom:1px}
.card.featured a{color:var(--green)}
.badge{width:156px;height:156px;z-index:3}

/* contact */
.field{background:#fff;height:34px;font-size:10px;color:#888;padding:10px 10px;box-shadow:0 1px 3px rgba(0,0,0,.05)}
.send{left:551px;top:2331px;width:96px;height:33px;background:var(--green);color:#fff;font-family:"Poppins",sans-serif;font-size:10px;font-weight:600;display:flex;align-items:center;justify-content:center;gap:6px;border:1px solid #fff}

/* footer */
.footer-brand{left:155px;top:2548px;display:flex;align-items:center;gap:12px;color:#fff;font-family:"Poppins",sans-serif;font-weight:600;font-size:22px}
.footer-brand i{width:28px;height:28px;background:var(--green);display:block}
.col-head{font-family:"Poppins",sans-serif;font-size:14px;font-weight:600;color:#fff}
.col-text{font-size:12.5px;line-height:19px;color:#b6b9be}
.col-text u{text-decoration:underline}
.social{left:860px;top:2554px;display:flex;gap:9px}
.social span{width:32px;height:32px;border-radius:50%;border:1px solid var(--green);display:block}
.social .on{background:var(--green)}
.rule{left:155px;width:890px;top:2647px;border-top:1px solid #3d4147}
.copyright{left:155px;top:2669px;font-size:12px;color:#b6b9be}
.foot-nav{left:600px;top:2670px;display:flex;gap:26px;font-family:"Poppins",sans-serif;font-size:10px;letter-spacing:.5px;color:#b6b9be}
.foot-nav .active{color:var(--green)}
.foot-nav .active::before{content:"-- "}
.foot-nav .active::after{content:" -"}
</style>
</head>
<body>

<div class="abs hero-photo" role="img" aria-label="Close-up photo of a calculator and pen on a desk, dark grey tones"></div>
<div class="abs cloud-photo" role="img" aria-label="Photo of mountain peaks above a sea of clouds"></div>

<svg class="abs shapes" width="1200" height="2711" viewBox="0 0 1200 2711" aria-hidden="true">
  <polygon points="0,200 434,506 0,560" fill="#3b9e3b" opacity=".88"/>
  <polygon points="0,560 1200,420 1200,905 0,905" fill="#ececee"/>
  <polygon points="0,560 1200,416 1200,436 0,568" fill="#3b9e3b"/>
  <polygon points="0,560 1200,416 1200,470 0,560" fill="#3b9e3b"/>
  <polygon points="0,904 1200,795 1200,840 0,906" fill="#4f555d"/>
  <polygon points="0,906 1200,840 1200,1140 0,1266" fill="#ffffff"/>
  <polygon points="0,2462 1200,2348 1200,2372 0,2472" fill="#3b9e3b"/>
  <polygon points="0,2470 1200,2370 1200,2711 0,2711" fill="#2b2e33"/>
  <!-- slider arrows -->
  <polygon points="1014,352 1000,345 1000,359" fill="#fff" transform="rotate(180 1007 352)"/>
  <polygon points="1030,352 1016,345 1016,359" fill="#3b9e3b"/>
  <polygon points="500,746 515,737 515,755" fill="#4f555d"/>
  <polygon points="715,746 700,737 700,755" fill="#3b9e3b"/>
  <!-- back to top -->
  <polygon points="1032,2666 1044,2686 1032,2680 1020,2686" fill="#3b9e3b"/>
</svg>

<header class="layer">
  <div class="abs brand layer"><span class="brand-mark"></span>Tallowmere Ledger</div>
  <nav class="abs main-nav layer"><span class="active">HOME</span><span>ABOUT US</span><span>OUR SERVICES</span><span>CONTACT US</span></nav>
  <div class="abs phone layer">Call Us: 0400 118 542</div>
  <div class="abs login layer"><i></i>LOGIN</div>
</header>

<section class="layer">
  <h1 class="abs hero-title layer">Tallowmere Ledger specialises<br>in providing quality</h1>
  <p class="abs hero-copy layer">outsourced financial management solutions (ranging from bookkeeping to financial controller...</p>
  <div class="abs btn-light layer">EXPLORE MORE</div>
  <div class="abs slide-dots layer"><span></span><span class="on"></span><span></span><span></span></div>
</section>

<section class="layer">
  <div class="abs quote-mark layer">&ldquo;</div>
  <p class="abs quote-text layer">Contrary to popular belief, Lorem Ipsum is not random text. It has roots in a piece of classical Latin literature from 45 BC, making it over 2000 years old, Harlan Voss.</p>
  <div class="abs quote-author layer"><b>Finibus</b><span>Standard Chunk</span></div>
</section>

<section class="layer">
  <div class="abs kicker layer" style="top:921px">WELCOME TO</div>
  <h2 class="abs title layer" style="top:935px">Tallowmere <em>Ledger</em></h2>
  <div class="abs dash layer" style="top:972px"></div>
  <p class="abs about-copy layer">Tallowmere Ledger originated with the idea of providing accounting services that would make clients feel safe and find refuge, feel confident that they could trust the numbers in their financial reports. The founders of Tallowmere Ledger migrated to Australia as refugees and the name of the business alludes to these origins. We strongly believe that every number counts...</p>
  <div class="abs btn-outline layer">EXPLORE MORE</div>
</section>

<section class="layer">
  <div class="abs kicker layer" style="top:1252px">WHAT WE DO</div>
  <h2 class="abs title layer" style="top:1266px">Our <em>Services</em></h2>
  <div class="abs dash layer" style="top:1303px"></div>

  <article class="abs card layer" style="left:155px;top:1413px"><h3>Bookkeeping</h3><p>Neque porro quisquam est qui dolo em ipsum quia dolor sit amet, consectetur...</p><a><span>CONTINUE READING</span></a></article>
  <article class="abs card featured layer" style="left:459px;top:1413px"><h3>Payroll</h3><p>Neque porro quisquam est qui dolo em ipsum quia dolor sit amet, consectetur...</p><a><span>CONTINUE READING</span></a></article>
  <article class="abs card layer" style="left:763px;top:1413px"><h3>Accounting</h3><p>Neque porro quisquam est qui dolo em ipsum quia dolor sit amet, consectetur...</p><a><span>CONTINUE READING</span></a></article>
  <article class="abs card layer" style="left:155px;top:1782px"><h3>Training</h3><p>Neque porro quisquam est qui dolo em ipsum quia dolor sit amet, consectetur...</p><a><span>CONTINUE READING</span></a></article>
  <article class="abs card layer" style="left:459px;top:1782px"><h3>Consulting</h3><p>Neque porro quisquam est qui dolo em ipsum quia dolor sit amet, consectetur...</p><a><span>CONTINUE READING</span></a></article>
  <article class="abs card layer" style="left:763px;top:1782px"><h3>Projects</h3><p>Neque porro quisquam est qui dolo em ipsum quia dolor sit amet, consectetur...</p><a><span>CONTINUE READING</span></a></article>

  <!-- bookkeeping -->
  <svg class="abs badge" style="left:217px;top:1330px" viewBox="0 0 156 156" aria-hidden="true">
    <circle cx="78" cy="78" r="76" fill="none" stroke="#3b9e3b" stroke-dasharray="2 3"/>
    <circle cx="78" cy="78" r="68" fill="#fff" stroke="#3b9e3b" stroke-width="2"/>
    <g fill="none" stroke="#4f555d" stroke-width="3"><rect x="52" y="50" width="42" height="52" rx="3"/><line x1="60" y1="62" x2="84" y2="62"/><line x1="60" y1="72" x2="80" y2="72"/><circle cx="96" cy="82" r="12"/></g>
    <rect x="46" y="84" width="22" height="26" rx="2" fill="#4f555d"/>
    <text x="96" y="87" font-family="Poppins,sans-serif" font-size="14" text-anchor="middle" fill="#4f555d">$</text>
  </svg>
  <!-- payroll -->
  <svg class="abs badge" style="left:521px;top:1330px" viewBox="0 0 156 156" aria-hidden="true">
    <circle cx="78" cy="78" r="72" fill="#fff" stroke="#3b9e3b" stroke-width="8"/>
    <rect x="64" y="46" width="36" height="54" fill="#7dc57d"/>
    <rect x="58" y="52" width="36" height="54" fill="#55b055"/>
    <rect x="52" y="58" width="36" height="54" fill="#3b9e3b"/>
    <text x="70" y="94" font-family="Poppins,sans-serif" font-size="22" font-weight="600" text-anchor="middle" fill="#fff">$</text>
  </svg>
  <!-- accounting -->
  <svg class="abs badge" style="left:825px;top:1330px" viewBox="0 0 156 156" aria-hidden="true">
    <circle cx="78" cy="78" r="76" fill="none" stroke="#3b9e3b" stroke-dasharray="2 3"/>
    <circle cx="78" cy="78" r="68" fill="#fff" stroke="#3b9e3b" stroke-width="2"/>
    <rect x="54" y="48" width="38" height="56" rx="3" fill="none" stroke="#4f555d" stroke-width="3"/>
    <rect x="66" y="44" width="14" height="8" fill="#4f555d"/>
    <circle cx="68" cy="84" r="8" fill="#4f555d"/>
    <rect x="80" y="72" width="24" height="34" rx="2" fill="#4f555d"/>
  </svg>
  <!-- training -->
  <svg class="abs badge" style="left:217px;top:1699px" viewBox="0 0 156 156" aria-hidden="true">
    <circle cx="78" cy="78" r="76" fill="none" stroke="#3b9e3b" stroke-dasharray="2 3"/>
    <circle cx="78" cy="78" r="68" fill="#fff" stroke="#3b9e3b" stroke-width="2"/>
    <rect x="70" y="50" width="40" height="30" fill="none" stroke="#4f555d" stroke-width="3"/>
    <line x1="90" y1="80" x2="90" y2="108" stroke="#4f555d" stroke-width="3"/>
    <circle cx="56" cy="58" r="7" fill="#4f555d"/>
    <path d="M46 70h18l10 8-3 4-9-6v34h-6V92h-4v18h-6z" fill="#4f555d"/>
  </svg>
  <!-- consulting -->
  <svg class="abs badge" style="left:521px;top:1699px" viewBox="0 0 156 156" aria-hidden="true">
    <circle cx="78" cy="78" r="76" fill="none" stroke="#3b9e3b" stroke-dasharray="2 3"/>
    <circle cx="78" cy="78" r="68" fill="#fff" stroke="#3b9e3b" stroke-width="2"/>
    <g fill="#4f555d"><circle cx="78" cy="54" r="7"/><path d="M66 74a12 10 0 0 1 24 0z"/><circle cx="58" cy="88" r="7"/><path d="M46 108a12 10 0 0 1 24 0z"/><circle cx="98" cy="88" r="7"/><path d="M86 108a12 10 0 0 1 24 0z"/></g>
    <path d="M78 76v6M78 82l-14 4M78 82l14 4" stroke="#4f555d" stroke-width="2" fill="none"/>
  </svg>
  <!-- projects -->
  <svg class="abs badge" style="left:825px;top:1699px" viewBox="0 0 156 156" aria-hidden="true">
    <circle cx="78" cy="78" r="76" fill="none" stroke="#3b9e3b" stroke-dasharray="2 3"/>
    <circle cx="78" cy="78" r="68" fill="#fff" stroke="#3b9e3b" stroke-width="2"/>
    <g fill="none" stroke="#4f555d" stroke-width="3"><rect x="50" y="56" width="56" height="44"/><path d="M46 52v52h6"/><polyline points="60,88 72,76 82,82 96,66"/></g>
  </svg>
</section>

<section class="layer">
  <div class="abs kicker layer" style="top:2094px">NEED HELP?</div>
  <h2 class="abs title layer" style="top:2106px">Contact <em>Us</em></h2>
  <div class="abs dash layer" style="top:2143px"></div>
  <div class="abs field layer" style="left:231px;top:2172px;width:235px">Name:</div>
  <div class="abs field layer" style="left:481px;top:2172px;width:236px">Email:</div>
  <div class="abs field layer" style="left:732px;top:2172px;width:236px">Phone:</div>
  <div class="abs field layer" style="left:231px;top:2223px;width:737px;height:86px">Message...</div>
  <div class="abs send layer">
    <svg width="10" height="10" viewBox="0 0 10 10" aria-hidden="true"><polygon points="0,5 10,0 7,10 5,6" fill="#fff"/></svg>SEND
  </div>
</section>

<footer class="layer">
  <div class="abs footer-brand layer"><i></i>Tallowmere<br>Ledger</div>
  <div class="abs layer" style="left:360px;top:2522px">
    <div class="col-head">Call Us:</div>
    <div class="col-text" style="margin-top:8px">0400 - 118 - 542<br><u>hello@tallowmereledger.com.au</u></div>
  </div>
  <div class="abs layer" style="left:632px;top:2522px">
    <div class="col-head">Locations:</div>
    <div class="col-text" style="margin-top:8px">4/88 Wren Street,<br>Marrickville NSW 2204</div>
  </div>
  <div class="abs layer" style="left:860px;top:2522px"><div class="col-head">Get Social:</div></div>
  <div class="abs social layer"><span></span><span class="on"></span><span></span><span></span></div>
  <div class="abs rule layer"></div>
  <div class="abs copyright layer">&copy; 2017 Tallowmere Ledger. All rights reserved.</div>
  <nav class="abs foot-nav layer"><span class="active">HOME</span><span>ABOUT US</span><span>OUR SERVICES</span><span>CONTACT US</span></nav>
</footer>

</body>
</html>
```